I need a business card design to compliment my existing branding [website and book give clear guidance here]. I teach business owners and managers how to become pioneers of business innovation in their industry - to challenge the paradigms and make their competition irrelevant. They will never look at business in the same way again.

The brand stands for innovation - to intelligently challenge the paradigms of each industry and seek to cause disruption. It's as provocative as it is progressive and many clients say that they find it quite uncomfortable to start with - they grow to love it and feel liberated by it.

The astronaut is the leading theme as it represents the pioneer, the maverick, the progressive ones. The astronaut can be as per the logo i.e. with the circle etc. or, can be extracted and used in isolation.

The word 'Masterclass' should not be used on the business card [even though it's in the attached logo].

Target Market(s)

Small to medium business owners, entrepreneurs, 'hungry' employees who want to accelerate their career

Industry/Entity Type

Business

Contact Information for Business Card

You. Leading Bold New Thinking.

Ned Farrow
Chief Innovation Coach

+61 [0]491 570 006
ned.farrow@coppermethodfinches.com
coppermethodfinches.com

Font styles to use
Other font styles liked:
• Eurostile

Requirements
Must have
• Simplistic and elegant is welcome.
• Colours and design must compliment the brand as per the attached documents - the book is probably the best guide as it is handed out at the same time as the business cards [whereas the website is looked at in isolation].
• I find the red stripe across the book cover quite striking.
• Font is Eurostile
Nice to have
• Unusual and eye catching but simple
Should not have
• No space scene in the background [i.e. it should not mimic the website banner]
• Other fonts than Eurostile

```html
<!DOCTYPE html>
<html lang="en">
<head>
<meta charset="utf-8">
<title>Copper Finches – Business Card</title>
<link href="https://fonts.googleapis.com/css2?family=Exo+2:wght@400;600&family=Michroma&display=swap" rel="stylesheet">
<style>
  :root {
    --paper: #ecebe8;
    --white: #ffffff;
    --navy: #1f3a4d;
    --coral: #e8605e;
    --butter: #f5e58c;
    --sun: #f2c94c;
    --teal: #4fa3a0;
    --teal-text: #3f9a96;
    --shadow: rgba(20, 30, 40, 0.18);
  }
  * { box-sizing: border-box; margin: 0; padding: 0; }
  html, body {
    width: 1200px; height: 849px; overflow: hidden;
    background: var(--paper);
  }
  .sheet {
    position: relative; width: 1200px; height: 849px;
    display: flex; align-items: center; justify-content: center; gap: 60px;
  }
  .card {
    position: relative; width: 520px; height: 300px; overflow: hidden;
    box-shadow: 0 10px 28px var(--shadow);
  }

  /* ---------- front ---------- */
  .card--front { background: var(--white); }
  .front__brand {
    position: absolute; left: 0; top: 0; width: 190px; height: 300px;
    padding: 62px 0 0 22px;
  }
  .brand-lockup { display: flex; align-items: center; gap: 10px; }
  .brand-lockup__dot {
    width: 34px; height: 34px; border-radius: 50%; background: var(--navy); flex: none;
  }
  .brand-lockup__name {
    font-family: "Michroma", sans-serif; color: var(--navy);
    font-size: 11px; line-height: 1.35; letter-spacing: 0.06em; text-transform: uppercase;
  }
  .tagline {
    position: absolute; left: 22px; bottom: 28px;
    font-family: "Exo 2", sans-serif; font-weight: 600; color: var(--teal-text);
    font-size: 14px; line-height: 1.2;
  }
  .front__panel { position: absolute; left: 190px; top: 0; width: 330px; height: 300px; }
  .panel__sky { position: absolute; inset: 0 0 auto 0; height: 118px; background: var(--navy); }
  .panel__hero {
    position: absolute; left: 70px; top: 14px; width: 120px; height: 104px;
    border-radius: 60px 60px 0 0;
    background: radial-gradient(circle at 50% 75%, var(--sun) 0 52%, #e9dcc0 78%, var(--navy) 100%);
  }
  .panel__stripe {
    position: absolute; left: 0; top: 118px; width: 330px; height: 54px;
    background: var(--coral); padding: 9px 0 0 56px;
  }
  .holder__name {
    font-family: "Michroma", sans-serif; color: var(--white);
    font-size: 14px; letter-spacing: 0.04em; text-transform: uppercase;
  }
  .holder__role {
    font-family: "Exo 2", sans-serif; font-weight: 600; color: var(--butter);
    font-size: 13px; margin-top: 2px;
  }
  .panel__ground { position: absolute; left: 0; top: 172px; width: 330px; height: 128px; background: var(--butter); }
  .panel__ground::before {
    content: ""; position: absolute; left: 0; top: 0; width: 330px; height: 20px; background: var(--navy);
  }
  .panel__scene {
    position: absolute; left: 18px; bottom: 12px; width: 52px; height: 46px; border-radius: 4px;
    background: linear-gradient(180deg, #cfd8dc, var(--coral));
  }
  .contact {
    position: absolute; right: 20px; top: 32px; text-align: right; list-style: none;
    font-family: "Exo 2", sans-serif; color: var(--navy); font-size: 12.5px; line-height: 1.45;
  }

  /* ---------- back ---------- */
  .card--back {
    background: var(--teal);
    display: flex; align-items: center; justify-content: center;
  }
  .card--back .brand-lockup { flex-direction: column; gap: 14px; }
  .card--back .brand-lockup__dot { width: 64px; height: 64px; }
  .card--back .brand-lockup__name { font-size: 22px; letter-spacing: 0.08em; }
</style>
</head>
<body>
<main class="sheet">
  <section class="card card--front" aria-label="Business card front">
    <div class="front__brand">
      <div class="brand-lockup">
        <span class="brand-lockup__dot"></span>
        <span class="brand-lockup__name">Copper<br>Finches</span>
      </div>
      <p class="tagline">You.<br>Leading<br>Bold New<br>Thinking.</p>
    </div>
    <div class="front__panel">
      <div class="panel__sky"></div>
      <div class="panel__hero" role="img" aria-label="Illustration of an astronaut in front of a yellow sun"></div>
      <div class="panel__stripe">
        <p class="holder__name">+ Ned Farrow</p>
        <p class="holder__role">Chief Innovation Coach</p>
      </div>
      <div class="panel__ground">
        <div class="panel__scene" role="img" aria-label="Illustration of a satellite dish on a small planet"></div>
        <ul class="contact">
          <li>+61 [0]491 570 006</li>
          <li>ned.farrow@coppermethodfinches.com</li>
          <li>coppermethodfinches.com</li>
        </ul>
      </div>
    </div>
  </section>

  <section class="card card--back" aria-label="Business card back">
    <div class="brand-lockup">
      <span class="brand-lockup__dot"></span>
      <span class="brand-lockup__name">Copper Finches</span>
    </div>
  </section>
</main>
</body>
</html>
```